Publisher needs a book cover design for ‘Lanterns Over the Marsh Gate’ book

We need a book cover (front, back, spine) for the 2nd edition of a book entitled ‘Lanterns Over the Marsh Gate’ and subtitled ‘the quiet geography of tidal winds, ferry routes and harbour lanterns’ (inverted commas not to be part of the title and subtitle). The author is Rupert Calloway. The publisher is Vellmark Press. The finished size of the paperback version will be the industry standard 9" x 6". There will be paperback, hardback, and e-book versions. The final number of pages is expected to be in the region 150-180 pages. Text for the back cover is not yet available, but at the bottom of the back cover should be publisher logo (rectangular) on the left and space for the ISBN bar code on the right. The circular logo should be on the spine. The design should be original and not include any stock images that have been created by someone else or may require obtaining a copyright licence to use. Symbols in common use and not copyrighted are probably ok. There are no required images, photographs or symbols except the publisher logo at the left bottom of the back cover and lower spine. Spine lettering should be UK/US style with the top of the writing nearest the front cover. The designer is free to be creative using appropriate diagrams, symbols or abstract designs. Rectangular and circular variants of the publisher logo are attached. Designers are assured that when evaluating designs absolutely no notice whatsoever is taken of a designer's Pixo Rally ranking or status; We are completely output driven, so what matters is the design, not the ranking or status of the designer. In a similar way, designs are not evaluated as 'good' or 'bad' - the winning design will be chosen after review by a design review panel and is not decided arbitrarily by a single person. All submitted designs should be capable of effective copyright assignment.

Target Market(s)

Practitioners, parents, teachers, pupils and academics concerned with child protection, safeguarding and the elimination of emotional abuse of children in the classroom

Font styles to use
Serif
Sans Serif

Requirements
Must have
• • Title, author, edition, subtitle, publisher logo
Nice to have
• • Originality, innovation
Should not have
• • Stock images or anything else requiring additional copyright discussions and negotiations.

```html
<!DOCTYPE html>
<html lang="en">
<head>
<meta charset="utf-8">
<title>Lanterns Over the Marsh Gate — Cover Spread</title>
<link href="https://fonts.googleapis.com/css2?family=GFS+Didot&family=Sorts+Mill+Goudy&display=swap" rel="stylesheet">
<style>
  :root {
    --paper: #ffffff;
    --ink: #111111;
    --plum: #8e2a64;
    --photo-rose: #b8407e;
    --photo-mauve: #9a5d95;
    --photo-teal: #8fc6b6;
    --block: #000000;
  }
  * { margin: 0; padding: 0; box-sizing: border-box; }
  html, body { width: 1200px; height: 880px; overflow: hidden; background: var(--paper); }
  .spread { position: relative; width: 1200px; height: 880px; background: var(--paper); color: var(--ink); }

  .title {
    position: absolute;
    font-family: "GFS Didot", "Didot", serif;
    font-weight: 400;
    font-size: 70px;
    line-height: 66px;
    letter-spacing: -0.5px;
  }
  .back-title { left: 49px; top: 26px; }
  .front-title { left: 652px; top: 26px; }

  .back-blurb {
    position: absolute;
    left: 45px; top: 281px; width: 510px;
    font-family: "Sorts Mill Goudy", "Goudy Old Style", serif;
    font-size: 17.6px;
    line-height: 26.7px;
    text-align: justify;
    hyphens: auto;
  }

  .publisher-mark {
    position: absolute;
    left: 45px; top: 774px;
    display: flex; align-items: center; gap: 8px;
  }
  .publisher-mark .dot { width: 48px; height: 48px; border-radius: 50%; background: var(--ink); }
  .publisher-mark .name {
    font-family: "Sorts Mill Goudy", serif;
    font-size: 26px; letter-spacing: 1px; color: var(--ink);
  }

  .isbn-space { position: absolute; left: 367px; top: 728px; width: 193px; height: 116px; background: var(--block); }

  .spine {
    position: absolute; left: 580px; top: 0; width: 36px; height: 880px;
  }
  .spine-line {
    position: absolute; left: 0; top: 44px; width: 36px; height: 740px;
    writing-mode: vertical-rl;
    display: flex; align-items: center;
    font-family: "GFS Didot", serif;
  }
  .spine-title { font-size: 29px; line-height: 36px; white-space: nowrap; }
  .spine-edition {
    font-family: "Sorts Mill Goudy", serif;
    font-size: 15px; color: var(--plum); margin-top: 26px; white-space: nowrap;
  }
  .spine-author {
    font-family: "Sorts Mill Goudy", serif;
    font-size: 24px; font-weight: 700; margin-top: 60px; white-space: nowrap;
  }
  .spine-mark {
    position: absolute; left: 9px; top: 800px; width: 18px; height: 18px;
    border-radius: 50%; background: var(--ink);
  }

  .edition {
    position: absolute; left: 658px; top: 238px;
    font-family: "Sorts Mill Goudy", serif;
    font-size: 19px; color: var(--plum); letter-spacing: 0.3px;
  }
  .subtitle {
    position: absolute; left: 653px; top: 281px; width: 420px;
    font-family: "Sorts Mill Goudy", serif;
    font-size: 21.5px; line-height: 23.5px;
  }
  .cover-image {
    position: absolute; left: 618px; top: 338px; width: 582px; height: 489px;
    background:
      linear-gradient(160deg, rgba(143,198,182,0.55) 0%, rgba(143,198,182,0) 45%),
      linear-gradient(180deg, var(--photo-mauve) 0%, var(--photo-rose) 45%, var(--photo-mauve) 75%, var(--photo-teal) 100%);
  }
  .author {
    position: absolute; left: 654px; top: 826px;
    font-family: "Sorts Mill Goudy", serif;
    font-size: 29px; font-weight: 700;
  }
</style>
</head>
<body>
<main class="spread">
  <section class="back-cover">
    <h2 class="title back-title">Lanterns<br>Over the<br>Marsh Gate</h2>
    <p class="back-blurb">Lorem Ipsum is simply dummy text of the printing and typesetting industry. Lorem Ipsum has been the industry's standard dummy text ever since the 1500s, when an unknown printer took a galley of type and scrambled it to make a type specimen book. It has survived not only five centuries, but also the leap into electronic typesetting, remaining essentially unchanged. It was popularised in the 1960s with the release of Tyreline sheets containing Lorem Ipsum passages, and more recently with desktop publishing software like Quillset Layout including versions of Lorem Ipsum.</p>
    <div class="publisher-mark"><span class="dot"></span><span class="name">VELLMARK PRESS</span></div>
    <div class="isbn-space"></div>
  </section>

  <section class="spine">
    <div class="spine-line">
      <span class="spine-title">Lanterns Over the Marsh Gate</span>
      <span class="spine-edition">2ND EDITION</span>
      <span class="spine-author">Rupert Calloway</span>
    </div>
    <span class="spine-mark" aria-label="Vellmark Press"></span>
  </section>

  <section class="front-cover">
    <h1 class="title front-title">Lanterns<br>Over the<br>Marsh Gate</h1>
    <p class="edition">2ND EDITION</p>
    <p class="subtitle">the quiet geography of tidal winds, ferry routes and harbour lanterns</p>
    <div class="cover-image" role="img" aria-label="Duotone photograph in rose and teal of empty rows of desks and benches"></div>
    <p class="author">Rupert Calloway</p>
  </section>
</main>
</body>
</html>
```